Desing for a packaging with 6 faces about an eye massager product

Hello I need fresh and new desing for this packaging. This packaging is for an eye massager the product help to reduce stress, eye fatigue, and he Reduces dark circles and tones the skin. The main color to the design need to be around this color: 8acdbf There is 6 faces to desing, the size are on the sample packaging (the 6 is for the back and the back have same size to the front 145 * 190mm) The most of text (long text) need to be in 2 line 1 line in English and 1 line in French. For more details see the ZIP.

Font styles to use
Sans Serif

Colors

Designer to choose colors to be used in the design.

Requirements
Must have
• All details writen inside the instruction doc + I need print ready file + Editable Source file from adobe software AI, PS…
Nice to have
• I need an mockup to the box

```html
<!DOCTYPE html>
<html lang="en">
<head>
<meta charset="utf-8">
<title>Lumo-Calm Packaging – Front and Spine</title>
<link rel="stylesheet" href="https://fonts.googleapis.com/css2?family=Maven+Pro:wght@400;500;700&family=Roboto:wght@400;500&display=swap">
<style>
  :root {
    --stage: #c9c9c9;
    --panel: #ffffff;
    --spine: #f1f1f1;
    --teal: #6cc3b0;
    --ink: #3a3a3a;
    --grey: #7b7b7b;
    --icon: #8d8d8d;
    --label: #9a9a9a;
    --band: #8f8070;
  }
  * { margin: 0; padding: 0; box-sizing: border-box; }
  html, body { width: 1200px; height: 834px; overflow: hidden; }
  body { background: var(--stage); font-family: "Maven Pro", sans-serif; position: relative; }

  .pack { position: absolute; left: 110px; top: 112px; display: flex; height: 610px; }

  .spine {
    width: 170px; height: 100%; background: var(--spine);
    display: flex; align-items: center; justify-content: center;
  }
  .spine__brand {
    writing-mode: vertical-rl; display: flex; flex-direction: row; align-items: center; gap: 6px;
  }
  .spine__name { font-size: 34px; font-weight: 500; color: var(--ink); letter-spacing: 1px; }
  .spine__tagline { font-family: "Roboto", sans-serif; font-size: 9px; font-weight: 500; color: var(--ink); letter-spacing: 1px; }

  .front { width: 840px; height: 100%; background: var(--panel); position: relative; }

  .front__product {
    position: absolute; left: 275px; top: 150px; width: 390px; height: 260px;
    border-radius: 48% 48% 44% 44% / 38% 38% 60% 60%;
    background: radial-gradient(ellipse at 50% 70%, #ffffff 0%, #eeeeee 60%, #cfc6bd 100%);
  }

  .front__title { position: absolute; left: 108px; top: 484px; font-size: 40px; font-weight: 400; color: var(--ink); letter-spacing: 0.5px; }
  .front__tagline-en { position: absolute; left: 112px; top: 538px; font-size: 17px; color: var(--teal); }
  .front__tagline-fr { position: absolute; left: 112px; top: 560px; font-size: 17px; color: var(--grey); }

  .features { position: absolute; right: 38px; top: 282px; width: 92px; list-style: none; }
  .feature { height: 40px; display: flex; flex-direction: column; align-items: center; justify-content: flex-start; }
  .feature svg { width: 20px; height: 18px; stroke: var(--icon); fill: none; stroke-width: 1.3; }
  .feature__label { font-family: "Roboto", sans-serif; font-size: 7.5px; color: var(--label); margin-top: 3px; white-space: nowrap; }
</style>
</head>
<body>
  <div class="pack">
    <section class="spine">
      <div class="spine__brand">
        <span class="spine__name">Lumora Care</span>
        <span class="spine__tagline">MEDICAL INNOVATION</span>
      </div>
    </section>

    <section class="front">
      <div class="front__product" role="img" aria-label="Product photo of a white eye massager with a taupe head strap"></div>

      <h1 class="front__title">Lumo-Calm™</h1>
      <p class="front__tagline-en">Better than a massage, an unique experience</p>
      <p class="front__tagline-fr">Plus qu'un massage, Une experience unique</p>

      <ul class="features">
        <li class="feature">
          <svg viewBox="0 0 20 18"><path d="M10 1v8M7 6l3 3 3-3M3 12h14M3 15h14"/></svg>
          <span class="feature__label">Air pressure</span>
        </li>
        <li class="feature">
          <svg viewBox="0 0 20 18"><path d="M2 6l3-3 3 3 3-3 3 3 3-3M2 11l3-3 3 3 3-3 3 3 3-3M2 16l3-3 3 3 3-3 3 3 3-3"/></svg>
          <span class="feature__label">Vibration Mode</span>
        </li>
        <li class="feature">
          <svg viewBox="0 0 20 18"><circle cx="10" cy="9" r="6"/><path d="M8 9h4"/></svg>
          <span class="feature__label">Wireless for music</span>
        </li>
        <li class="feature">
          <svg viewBox="0 0 20 18"><circle cx="10" cy="9" r="7"/><path d="M7 9h6"/></svg>
          <span class="feature__label">180 % Fold</span>
        </li>
        <li class="feature">
          <svg viewBox="0 0 20 18"><circle cx="7" cy="5" r="3"/><circle cx="13" cy="13" r="3"/><path d="M9 7l2 4"/></svg>
          <span class="feature__label">Easy Moving</span>
        </li>
        <li class="feature">
          <svg viewBox="0 0 20 18"><rect x="2" y="5" width="14" height="8"/><path d="M16 8h2v2h-2M5 7v4M8 7v4M11 7v4"/></svg>
          <span class="feature__label">Battery Lithium</span>
        </li>
        <li class="feature">
          <svg viewBox="0 0 20 18"><path d="M9 2h2v10H9z"/><circle cx="10" cy="14" r="2.5"/></svg>
          <span class="feature__label">Hot Compress</span>
        </li>
      </ul>
    </section>
  </div>
</body>
</html>
```